Regional health service needs a PowerPoint design

We are a new organisation responsible for the purchasing of health services for the population of Marrowfield and Kelton in Essex, UK - a population of c.300,000.

We are looking for a set of powerpoint master slides for use principally as 'talk books' and reports for presenting information regarding the performance of the organisation externally and to use as the basis for producing internal reports and communications.

We would like to see designs which portray the organisation as being new and different from historic CHW organisations, whilst following the principles outlined within National CHW brand guidelines (see attached). The slides should communicate creativity and professionalism.

Our logo is available on request (due to technical issues, we cannot upload onto here).

Our brand guidelines are available at:
http://www.carewellmarks.example/all-guidelines/guidelines/authorised-clinical-commissioning-groups/introduction

An example report (which we would look to move over to our new template) is available at:
http://www.marrowfieldandkeltonhcb.example/key-documents/doc_download/142-integrated-plan-2013-15

Further information on us is available on our website: www.marrowfieldandkeltonhcb.example

Target Market(s)

Target audience is healthcare professionals and the general public.

Industry/Entity Type

Health

Requirements
Must have
• Include the organisations logo and provide a cover sheet front page and 3/4 slides showing how reports could be structured (e.g. narrative and graphical information / tabular information / use of photos etc).

Typefaces and colour schemes should be in line with our brand guidelines (i.e. principal use of Arial). Our guidelines are available at:

Nice to have
• As an organisation we are made up of four localities, it would be good to see designs that draw on this element of our organisation.

```html
<!DOCTYPE html>
<html lang="en">
<head>
<meta charset="utf-8">
<title>Integrated Plan 2013-15 – Slide Masters</title>
<link href="https://fonts.googleapis.com/css2?family=Arimo:wght@400;700&display=swap" rel="stylesheet">
<style>
:root{
  --blue:#0a6fc2;
  --blue-dark:#00508f;
  --navy:#0b2f57;
  --grey-box:#7a7a7a;
  --text-blue:#1a74c4;
  --org-name:#1c3f8c;
  --row-a:#d5dcea;
  --row-b:#e8ecf4;
}
*{box-sizing:border-box;margin:0;padding:0}
html,body{width:1200px;height:724px;overflow:hidden;background:#fff;font-family:"Arimo",Arial,sans-serif}
.canvas{position:relative;width:1200px;height:724px}
.slide{position:absolute;width:385px;height:290px;background:#fff;overflow:hidden;box-shadow:1px 2px 5px rgba(0,0,0,.35)}
.s1{left:8px;top:47px}.s2{left:405px;top:47px}.s3{left:805px;top:47px}
.s4{left:8px;top:387px}.s5{left:405px;top:387px}.s6{left:805px;top:387px}
.abs{position:absolute}

/* cover + closing */
.map-area{position:absolute;left:0;top:0;width:385px;height:213px;background:radial-gradient(ellipse at 55% 45%,#fafbfc 0%,#e9ecef 70%,#dcdfe3 100%)}
.map-area::after{content:"";position:absolute;inset:0;background:radial-gradient(ellipse at 60% 40%,rgba(120,160,205,.25),rgba(120,160,205,0) 60%)}
.cover-band{position:absolute;left:0;height:28px;background:var(--blue);color:#fff;font-weight:700;font-size:17px;line-height:28px;white-space:nowrap}
.cover-stripe{position:absolute;left:0;width:385px;height:6px;background:var(--blue)}
.contact{position:absolute;left:13px;font-size:6.5px;line-height:11px;color:#222}
.contact span{color:var(--text-blue)}
.org-name{position:absolute;text-align:right;color:var(--org-name);font-weight:700;line-height:1.2;white-space:nowrap}
.org-lg{right:12px;font-size:7.4px}
.org-sm{right:10px;bottom:11px;font-size:4.8px}

/* content slides */
.wash{position:absolute;left:0;top:38px;width:385px;height:242px;background:radial-gradient(ellipse at 55% 50%,#fff 0%,#f3f5f8 60%,#eceff3 100%)}
.header{position:absolute;left:0;top:0;width:385px;height:38px;background:var(--blue);color:#fff;font-weight:700;font-size:17px;padding:9px 12px}
.header.two{font-size:16px;line-height:16px;padding:1px 12px;height:36px}
.footer{position:absolute;left:0;bottom:3px;width:385px;height:7px;background:var(--blue);color:#fff;font-size:5px;line-height:7px}
.footer .date{position:absolute;left:10px}
.footer .conf{position:absolute;left:174px}
.footer .page{position:absolute;right:8px}

/* contents */
.toc-item{position:absolute;left:14px;width:300px;height:15px}
.toc-num{position:absolute;left:0;top:-2px;width:18px;height:18px;border-radius:50%;background:linear-gradient(#fff,#e2e6ea);border:1px dashed var(--blue);color:var(--blue-dark);font-size:8.5px;font-weight:700;text-align:center;line-height:16px;z-index:1}
.toc-bar{position:absolute;left:14px;top:1px;width:283px;height:12px;background:linear-gradient(#fdfdfd,#d9dcdf);border:1px dashed var(--blue);color:var(--text-blue);font-size:7.6px;line-height:10px;padding-left:16px;white-space:nowrap}

/* org chart */
.box{position:absolute;display:flex;align-items:center;justify-content:center;text-align:center;font-size:6px;line-height:1.2}
.box.dark{background:var(--grey-box);color:#fff;font-size:7px}
.box.board{background:linear-gradient(var(--blue),var(--blue-dark));color:#fff;font-weight:700;font-size:7px}
.box.light{background:linear-gradient(#fafafa,#d8d8d8);border:1px solid #9a9a9a;color:#222}
.box.blue{background:var(--blue);color:#fff}
.box .note{font-size:5px}
.links{position:absolute;left:0;top:0}

/* chart */
.chart-frame{position:absolute;left:44px;top:63px;width:294px;height:182px;border:1px dashed var(--blue);background:linear-gradient(#fff,#dcdfe2)}
.chart-title{position:absolute;left:0;top:12px;width:100%;text-align:center;color:var(--text-blue);font-weight:700;font-size:10px}

/* table */
.table-title{position:absolute;left:0;top:97px;width:385px;text-align:center;color:var(--text-blue);font-weight:700;font-size:11px}
.data-table{position:absolute;left:55px;top:122px;width:255px;border-collapse:separate;border-spacing:1px;font-size:9px;text-align:center}
.data-table th{background:var(--blue);color:#fff;font-weight:400;height:15px}
.data-table td{height:15px;color:#333}
.data-table tr:nth-child(odd) td{background:var(--row-a)}
.data-table tr:nth-child(even) td{background:var(--row-b)}

.sub-title{position:absolute;left:59px;top:123px;font-weight:700;font-size:11px;color:#111}
</style>
</head>
<body>
<div class="canvas">

<section class="slide s1">
  <div class="map-area" role="img" aria-label="Soft grey world map across the upper cover"></div>
  <div class="cover-band" style="top:90px;width:210px;padding-left:4px">Integrated Plan 2013-15</div>
  <div class="cover-stripe" style="top:213px"></div>
  <div class="contact" style="top:236px">
    <div><span>Contact:</span> Mr. Alan Pierce</div>
    <div><span>Address:</span> 72, Harlow Crescent, Dunmere</div>
    <div><span>Email:</span> alanpierce@chw.example</div>
    <div><span>Website:</span> www.chw.example</div>
  </div>
  <div class="org-name org-lg" style="top:246px">Marrowfield and Kelton<br>Clinical Commissioning Group</div>
</section>

<section class="slide s2">
  <div class="wash" role="img" aria-label="Faint world map behind the slide content"></div>
  <div class="header">Contents</div>
  <div class="toc-item" style="top:48px"><div class="toc-num">1</div><div class="toc-bar">Introduction to Marrowfield and Kelton CCG</div></div>
  <div class="toc-item" style="top:69.5px"><div class="toc-num">2</div><div class="toc-bar">The Health of our population</div></div>
  <div class="toc-item" style="top:91px"><div class="toc-num">3</div><div class="toc-bar">Our Strategy 2013-15</div></div>
  <div class="toc-item" style="top:112.5px"><div class="toc-num">4</div><div class="toc-bar">Challenges in our local system</div></div>
  <div class="toc-item" style="top:134px"><div class="toc-num">5</div><div class="toc-bar">Work programs to deliver the strategy</div></div>
  <div class="toc-item" style="top:155.5px"><div class="toc-num">6</div><div class="toc-bar">Finance Strategy and our Commissioning Intentions</div></div>
  <div class="toc-item" style="top:177px"><div class="toc-num">7</div><div class="toc-bar">Annual Operating Plan 2013/14</div></div>
  <div class="toc-item" style="top:198.5px"><div class="toc-num">8</div><div class="toc-bar">Risk Management &amp; Monitoring of Integrated Strategy</div></div>
  <div class="toc-item" style="top:220px"><div class="toc-num">9</div><div class="toc-bar">Commissioning Intentions 2013/14 Collaborative Arrangements</div></div>
  <div class="toc-item" style="top:241.5px"><div class="toc-num">10</div><div class="toc-bar">Appendices : How we are delivering national requirements</div></div>
  <div class="org-name org-sm">Marrowfield and Kelton<br>Clinical Commissioning Group</div>
  <div class="footer"><span class="date">02-08-2013</span><span class="conf">Confidential</span><span class="page">2</span></div>
</section>

<section class="slide s3">
  <div class="wash" role="img" aria-label="Faint world map behind the slide content"></div>
  <div class="header two">Marrowfield and Kelton CCG<br>Corporate Governance Structure</div>
  <svg class="links" width="385" height="290" viewBox="0 0 385 290">
    <g stroke="#8a8a8a" stroke-width="1.2" fill="none">
      <line x1="145" y1="71" x2="175" y2="91"/>
      <line x1="245" y1="70" x2="215" y2="91"/>
      <line x1="105" y1="104" x2="127" y2="104"/>
      <line x1="262" y1="104" x2="273" y2="104"/>
      <line x1="195" y1="166" x2="195" y2="185"/>
    </g>
  </svg>
  <div class="box dark" style="left:108px;top:48px;width:74px;height:23px">Corridor</div>
  <div class="box dark" style="left:210px;top:45px;width:80px;height:25px">Partnership and LIC</div>
  <div class="box dark" style="left:3px;top:93px;width:102px;height:22px">Kelton</div>
  <div class="box board" style="left:127px;top:91px;width:135px;height:27px">Marrowfield and Kelton<br>CCG Board</div>
  <div class="box dark" style="left:273px;top:90px;width:90px;height:25px">(South Wexmoor Managed Care) SWMC</div>
  <div class="box light" style="left:3px;top:134px;width:70px;height:32px">Audit Committee<br>(lay chair)</div>
  <div class="box light" style="left:81px;top:134px;width:70px;height:32px">Finance Committee<br>(GP chair)</div>
  <div class="box light" style="left:161px;top:134px;width:69px;height:32px">Clinical Executive –<br>Turnaround and<br>Transformation<br>(GP chair)</div>
  <div class="box light" style="left:238px;top:134px;width:70px;height:32px">Remuneration<br>Committee<br>(lay chair)</div>
  <div class="box light" style="left:311px;top:134px;width:70px;height:32px">Quality and<br>Governance<br>Committee<br>(Exec nurse chair)</div>
  <div class="box light" style="left:158px;top:185px;width:74px;height:28px">Acute Trust Commissioning<br>(GP clinical lead)</div>
  <div class="box blue" style="left:10px;top:220px;width:66px;height:42px">South Wexmoor<br>Collaborative<br>Group<br><span class="note">(4 x South Wexmoor CCGs)</span></div>
  <div class="box blue" style="left:83px;top:220px;width:68px;height:42px">Wexmoor Health<br>and Wellbeing<br>Board</div>
  <div class="box blue" style="left:161px;top:220px;width:69px;height:42px">Marrowfield Council –<br>Health and<br>Wellbeing Group</div>
  <div class="box blue" style="left:237px;top:220px;width:69px;height:42px">Kelton Council –<br>Health and<br>Wellbeing Group</div>
  <div class="box blue" style="left:311px;top:220px;width:68px;height:42px">Patients and<br>Public</div>
  <div class="org-name org-sm">Marrowfield and Kelton<br>Clinical Commissioning Group</div>
  <div class="footer"><span class="date">02-08-2013</span><span class="conf">Confidential</span><span class="page">3</span></div>
</section>

<section class="slide s4">
  <div class="wash" role="img" aria-label="Faint world map behind the slide content"></div>
  <div class="header">Graphic Slide</div>
  <div class="chart-frame">
    <div class="chart-title">Graphic Title</div>
    <svg class="abs" style="left:79px;top:47px" width="130" height="130" viewBox="0 0 130 130">
      <g transform="rotate(-90 65 65)" fill="none" stroke-width="32">
        <circle cx="65" cy="65" r="46" stroke="#0a6fc2" stroke-dasharray="170.53 289.03"/>
        <circle cx="65" cy="65" r="46" stroke="#000" stroke-dasharray="0 170.53 49.14 289.03"/>
        <circle cx="65" cy="65" r="46" stroke="#0b2f57" stroke-dasharray="0 219.67 34.68 289.03"/>
        <circle cx="65" cy="65" r="46" stroke="#7a7a7a" stroke-dasharray="0 254.35 34.68 289.03"/>
      </g>
      <g fill="#fff" font-size="8.5" text-anchor="middle" font-family="Arimo, Arial, sans-serif">
        <text x="110" y="80">59%</text>
        <text x="23" y="93">17%</text>
        <text x="22" y="62">12%</text>
        <text x="46" y="28">12%</text>
      </g>
    </svg>
  </div>
  <div class="org-name org-sm">Marrowfield and Kelton<br>Clinical Commissioning Group</div>
  <div class="footer"><span class="date">02-08-2013</span><span class="conf">Confidential</span><span class="page">4</span></div>
</section>

<section class="slide s5">
  <div class="wash" role="img" aria-label="Faint world map behind the slide content"></div>
  <div class="header">Table slide</div>
  <div class="table-title">Table Title</div>
  <table class="data-table">
    <thead><tr><th>Category A</th><th>Category B</th><th>Category C</th><th>Category D</th></tr></thead>
    <tbody>
      <tr><td>111.222</td><td>111.333</td><td>111.444</td><td>111.999</td></tr>
      <tr><td>222.333</td><td>222.444</td><td>222.333</td><td>222.333</td></tr>
      <tr><td>333.444</td><td>333.555</td><td>333.888</td><td>333.999</td></tr>
      <tr><td>444.555</td><td>444.222</td><td>444.777</td><td>444.555</td></tr>
      <tr><td>555.222</td><td>555.777</td><td>555.888</td><td>555.222</td></tr>
    </tbody>
  </table>
  <div class="org-name org-sm">Marrowfield and Kelton<br>Clinical Commissioning Group</div>
  <div class="footer"><span class="date">02-08-2013</span><span class="conf">Confidential</span><span class="page">5</span></div>
</section>

<section class="slide s6">
  <div class="map-area" style="height:221px" role="img" aria-label="Soft grey world map across the upper closing slide"></div>
  <div class="cover-band" style="top:91px;width:211px;padding-left:55px">THANK YOU</div>
  <div class="sub-title">FOR YOUR TIME</div>
  <div class="cover-stripe" style="top:221px"></div>
  <div class="contact" style="top:239px">
    <div><span>Contact:</span> Mr. Alan Pierce</div>
    <div><span>Address:</span> 72, Harlow Crescent, Dunmere</div>
    <div><span>Email:</span> alanpierce@chw.example</div>
    <div><span>Website:</span> www.chw.example</div>
  </div>
  <div class="org-name org-lg" style="top:255px">Marrowfield and Kelton<br>Clinical Commissioning Group</div>
</section>

</div>
</body>
</html>
```